Business card design needed

The company name is Wendale Architects. We are an architectural company based in Melbourne,Australia that has a mix of client base from health care, commercial office, aged care, multi-residential, single residential and retail. Design type is contemporary.

Suggest the base colours need to be black and white. Please leave an area on the back of the card available for handwritten notes.

Target Market(s)

Generally corporate, aged 30 to 65

Industry/Entity Type

Residential

Contact Information for Business Card

Wendale Architects
Mark Wendale
14 Pellow Street
Rosevale VIC 3071
T (03) 9512 4067
M 0438 617 295
E mw@wendalearc.com.au

Logo Text

WA

Logo styles of interest
Emblem Logo
Abstract Logo
Lettermark Logo
Requirements
Must have
• I am having trouble attaching a sketch so would really appreciate your effort to try the following brief.

Black and White (B&W)
Would like different card cutout profile. Logo Example, use the half circle curve of the G to form the left edge of the card with no margin. The A is to sit inside the G, connected to the G by its horizontal. The A has its cross bar and lower right leg removed. Card in black, text in white.

Back of card to be black text on white background with services provided.

Client Focused Service
Architecture and Design
Functional Planning
Town Planning
Feasability Studies
Contract Documentation
Contract Administration
Project Management

Simple elegant text, Ariel or similar
Nice to have
• Integrated logo and card cut-out.

Card base black on front, white on back
Should not have
• Too many colours
Fussy details

```html
<!DOCTYPE html>
<html lang="en">
<head>
<meta charset="utf-8">
<title>Wendale Architects – Business Card</title>
<link href="https://fonts.googleapis.com/css2?family=Arimo:wght@400;700&display=swap" rel="stylesheet">
<style>
  :root {
    --stage-blue: #0a3cf5;
    --card-black: #000000;
    --card-white: #ffffff;
    --ink-black: #000000;
    --ink-white: #ffffff;
    --shadow: rgba(0, 0, 0, 0.55);
  }
  html, body {
    margin: 0;
    padding: 0;
    width: 1200px;
    height: 1000px;
    overflow: hidden;
    background: var(--stage-blue);
  }
  .stage {
    display: block;
    width: 1200px;
    height: 1000px;
    font-family: "Arimo", Arial, sans-serif;
  }
  .card-shape { filter: drop-shadow(4px 6px 6px var(--shadow)); }
  .card-front { fill: var(--card-black); }
  .card-back { fill: var(--card-white); }
  .monogram { fill: var(--ink-white); font-weight: 700; font-size: 150px; }
  .company-name { fill: var(--ink-white); font-weight: 700; font-size: 26px; letter-spacing: 0.3px; }
  .person-name { fill: var(--ink-white); font-weight: 700; font-size: 22px; }
  .contact-line { fill: var(--ink-white); font-weight: 400; font-size: 18px; }
  .service-item { fill: var(--ink-black); font-weight: 400; font-size: 23px; }
</style>
</head>
<body>
<svg class="stage" viewBox="0 0 1200 1000" xmlns="http://www.w3.org/2000/svg" aria-label="Wendale Architects business card, front and back">
  <!-- Front of card -->
  <g class="front">
    <path class="card-shape card-front"
          d="M300 145 L825 145 L968 515 L320 515 C200 515 150 420 150 320 C150 215 215 145 300 145 Z"/>
    <text class="monogram" x="335" y="385" text-anchor="middle">WA</text>
    <text class="company-name" x="502" y="207">Wendale Architects</text>
    <text class="person-name" x="700" y="341">Mark Wendale</text>
    <g class="contact-block" text-anchor="end">
      <text class="contact-line" x="892" y="392">14 Pellow Street</text>
      <text class="contact-line" x="899" y="414">Rosevale VIC 3071</text>
      <text class="contact-line" x="908" y="437">T (03) 9512 4067</text>
      <text class="contact-line" x="916" y="459">M 0438 617 295</text>
      <text class="contact-line" x="926" y="482">E mw@wendalearc.com.au</text>
    </g>
  </g>

  <!-- Back of card -->
  <g class="back">
    <path class="card-shape card-back"
          d="M243 546 L760 546 C960 546 1078 670 1078 745 C1078 845 1005 914 905 914 L388 914 Z"/>
    <g class="services">
      <text class="service-item" x="543" y="639">• Client Focused Service</text>
      <text class="service-item" x="584" y="667">• Architecture and Design</text>
      <text class="service-item" x="677" y="695">• Functional Planning</text>
      <text class="service-item" x="760" y="723">• Town Planning</text>
      <text class="service-item" x="711" y="751">• Feasability Studies</text>
      <text class="service-item" x="653" y="779">• Contract Documentation</text>
      <text class="service-item" x="655" y="807">• Contract Administration</text>
      <text class="service-item" x="641" y="835">• Project Management</text>
    </g>
  </g>
</svg>
</body>
</html>
```